Offshore Energy Projects Management Consultancy needs a business card design

Logo available. We provide teams to deliver engineering consultancy, project management and delivery teams mainly in the offshore renewables sector. The company is all about bringing the right people to a project to deliver the scope.

The business card will be used for all staff.

The business card should be quite simple, vibrant and uncluttered but convey experience, enthusiasm and integration.

Target Market(s)

Energy Project Developers and Tier 1 construction companies

Contact Information for Business Card

Logo should be on the back of the card. I'm happy for the designer to play with the colour of the logo and background colour.

Front of the card should convey all the must have information in a clear and professional manner but without being overly traditional.

Colors

Designer to choose colors to be used in the design.

Requirements
Must have
• Land Line Tel Number, Mobile Tel Number, Email, business address, web address.

```html
<!DOCTYPE html>
<html lang="en">
<head>
<meta charset="utf-8">
<title>Tidewell Partners – Business Card</title>
<link href="https://fonts.googleapis.com/css2?family=Lato:ital,wght@0,300;0,400;0,700;0,900;1,300&display=swap" rel="stylesheet">
<style>
  :root {
    --page-bg: #ececec;
    --card-white: #ffffff;
    --brand-blue: #1a8fd4;
    --ink: #111111;
    --body-text: #2b2b2b;
    --muted: #c4c4c4;
    --label: #555555;
    --sea-top: #2f6a9a;
    --sea-mid: #5f97ad;
    --sea-haze: #8aa3ad;
    --sea-water: #2c5f8a;
    --on-photo: #ffffff;
  }
  * { box-sizing: border-box; margin: 0; padding: 0; }
  html, body {
    width: 1200px; height: 1200px; overflow: hidden;
    background: var(--page-bg);
    font-family: 'Lato', sans-serif;
  }
  .card {
    position: absolute;
    top: 466px;
    width: 491px;
    height: 273px;
  }
  .card--front { left: 40px; background: var(--card-white); }
  .card--back { left: 643px; overflow: hidden; }

  .brand-name {
    position: absolute;
    left: 50px; top: 44px;
    width: 200px;
    font-weight: 900;
    font-size: 30px;
    line-height: 1.05;
    color: var(--brand-blue);
    letter-spacing: -0.5px;
  }

  .contact {
    position: absolute;
    left: 294px; top: 36px;
    color: var(--body-text);
  }
  .contact__name {
    font-weight: 900;
    font-size: 21px;
    color: var(--ink);
    letter-spacing: -0.4px;
    line-height: 1.2;
  }
  .contact__role {
    font-weight: 300;
    font-size: 10.5px;
    color: var(--muted);
    margin-top: 1px;
  }
  .contact__lines {
    list-style: none;
    margin-top: 24px;
    font-size: 10.5px;
    font-weight: 300;
    line-height: 18.4px;
  }
  .contact__label { font-style: italic; color: var(--label); }
  .contact__address {
    font-style: normal;
    margin-top: 27px;
    font-size: 10.5px;
    font-weight: 300;
    line-height: 18.4px;
  }

  .back__photo {
    position: absolute; inset: 0;
    background:
      linear-gradient(180deg, rgba(0,0,0,0) 0%, rgba(0,0,0,0) 78%, var(--sea-water) 86%, #1f4d78 100%),
      radial-gradient(ellipse at 30% 35%, #6aa7bb 0%, rgba(106,167,187,0) 60%),
      linear-gradient(180deg, var(--sea-top) 0%, var(--sea-mid) 45%, var(--sea-haze) 78%);
  }
  .back__name {
    position: absolute;
    left: 0; right: 0; top: 92px;
    text-align: center;
    font-weight: 900;
    font-size: 34px;
    line-height: 1.1;
    color: var(--on-photo);
    letter-spacing: 0.5px;
  }
  .back__web {
    position: absolute;
    left: 0; right: 0; top: 221px;
    text-align: center;
    font-size: 10px;
    font-weight: 300;
    color: var(--on-photo);
  }
  .back__web b { font-weight: 700; }
</style>
</head>
<body>
  <section class="card card--front">
    <div class="brand-name">Tidewell Partners</div>
    <div class="contact">
      <div class="contact__name">Jonah Reid</div>
      <div class="contact__role">Director</div>
      <ul class="contact__lines">
        <li>+44 1632 960 418 <span class="contact__label">(Mobile)</span></li>
        <li>+44 1632 960 418 <span class="contact__label">(Land Line)</span></li>
        <li>hello@tidewell.ltd</li>
      </ul>
      <address class="contact__address">
        The Harbour Building,<br>
        12 Quay Road,<br>
        Portlen, PL4 2XQ
      </address>
    </div>
  </section>

  <section class="card card--back">
    <div class="back__photo" role="img" aria-label="Photograph of an offshore wind farm with turbines rising from a calm sea under a hazy blue sky"></div>
    <div class="back__name">Tidewell Partners</div>
    <div class="back__web">www.<b>tidewell</b>.ltd</div>
  </section>
</body>
</html>
```